The most modern business card ever !!!

Our company call “Vantilo”. Vantilo is a technology company specialized in cruises solutions. Out main product is a platform to reserve cruises. This is a revolutionary platform that make easier to travel agencies and final users to reserve cruises across dozen companies like tarvik, welbi, dpv, hbt, etc..We are a “start up”, with a young team of developers and we want to transmit it.. For it, we want something different, a modern business card that represent cruises and technology.. When someone receive this card, this person should say: wowww this is different… this is modern… this is a cruise related company..
Contact Information for Business Card
Requirements
Must have
- diferent, modern
Should not have
- traditions business card

```html
<!DOCTYPE html>
<html lang="en">
<head>
<meta charset="utf-8">
<title>Vantilo business card</title>
<link href="https://fonts.googleapis.com/css2?family=Exo+2:wght@400;500;600&display=swap" rel="stylesheet">
<style>
  :root {
    --page: #d8d8d5;
    --card-dark: #101010;
    --card-light: #ecebe8;
    --brand-blue: #2a9fd6;
    --name-blue: #2a9fd6;
    --role-green: #93b15e;
    --address-salmon: #e58a72;
    --contact-white: #f2f2f2;
    --logo-ink: #1c1c1c;
  }
  html, body {
    margin: 0;
    width: 1200px;
    height: 971px;
    overflow: hidden;
    background: var(--page);
    font-family: "Exo 2", sans-serif;
  }
  .card {
    position: absolute;
    left: 100px;
    top: 185px;
    width: 1000px;
    height: 600px;
    border-radius: 24px;
    overflow: hidden;
    box-shadow: 0 18px 40px rgba(0,0,0,0.18);
  }
  .card-shapes {
    position: absolute;
    inset: 0;
  }
  .holder-name {
    position: absolute;
    left: 70px;
    top: 150px;
    margin: 0;
    font-size: 36px;
    font-weight: 600;
    color: var(--name-blue);
  }
  .holder-role {
    position: absolute;
    left: 72px;
    top: 200px;
    margin: 0;
    font-size: 25px;
    font-weight: 400;
    color: var(--role-green);
  }
  .address {
    position: absolute;
    left: 72px;
    top: 285px;
    margin: 0;
    font-style: normal;
    font-size: 26px;
    line-height: 33px;
    color: var(--address-salmon);
  }
  .contacts {
    position: absolute;
    left: 72px;
    top: 440px;
    margin: 0;
    padding: 0;
    list-style: none;
    font-size: 26px;
    line-height: 33px;
    color: var(--contact-white);
  }
  .contacts li {
    display: flex;
    align-items: center;
    gap: 8px;
  }
  .contacts svg {
    width: 20px;
    height: 20px;
    flex: none;
  }
  .web-brand {
    color: var(--brand-blue);
    font-weight: 600;
  }
  .brand-name {
    position: absolute;
    left: 560px;
    top: 232px;
    margin: 0;
    font-size: 100px;
    font-weight: 500;
    letter-spacing: 2px;
    color: var(--logo-ink);
  }
</style>
</head>
<body>
  <section class="card">
    <svg class="card-shapes" viewBox="0 0 1000 600" width="1000" height="600" aria-hidden="true">
      <rect class="light-field" width="1000" height="600" fill="var(--card-light)"/>
      <polygon class="blue-chevron" points="632,0 690,0 495,330 818,600 760,600 440,330" fill="var(--brand-blue)"/>
      <polygon class="dark-field" points="0,0 600,0 405,330 728,600 0,600" fill="var(--card-dark)"/>
    </svg>

    <h1 class="holder-name">Daniel Moreau</h1>
    <p class="holder-role">Developer</p>

    <address class="address">
      R Almirante Tavora 148<br>
      Sala 17, Vila Mariana<br>
      Sao Bento, SP<br>
      04112-380, Brasil
    </address>

    <ul class="contacts">
      <li>
        <svg viewBox="0 0 24 24" aria-hidden="true"><path fill="var(--brand-blue)" d="M6.6 10.8c1.4 2.8 3.8 5.1 6.6 6.6l2.2-2.2c.3-.3.7-.4 1-.2 1.1.4 2.3.6 3.6.6.6 0 1 .4 1 1V20c0 .6-.4 1-1 1C10.6 21 3 13.4 3 4c0-.6.4-1 1-1h3.5c.6 0 1 .4 1 1 0 1.3.2 2.5.6 3.6.1.3 0 .7-.2 1l-2.3 2.2z"/></svg>
        (11) 9472-3185
      </li>
      <li>
        <svg viewBox="0 0 24 24" aria-hidden="true"><rect x="2.5" y="5" width="19" height="14" fill="none" stroke="var(--brand-blue)" stroke-width="2"/><path d="M3 6l9 7 9-7" fill="none" stroke="var(--brand-blue)" stroke-width="2"/></svg>
        rafa@vantilo.com.br
      </li>
      <li>
        <svg viewBox="0 0 24 24" aria-hidden="true"><g fill="none" stroke="var(--brand-blue)" stroke-width="1.6"><circle cx="12" cy="12" r="9.5"/><ellipse cx="12" cy="12" rx="4" ry="9.5"/><path d="M2.5 12h19M4 7h16M4 17h16"/></g></svg>
        <span>www.<span class="web-brand">vantilo</span>.com.br</span>
      </li>
    </ul>

    <p class="brand-name">Vantilo</p>
  </section>
</body>
</html>
```